Joomla Responsive Website Template for an International Biotechnology Company

Our client is a biotechnology company that uses silver-based technology to help make products antimicrobial, antibacterial, and anti fungal. We need a Joomla-based template that is responsive/mobile friendly when viewed on tablets or smartphones. We are looking for a template design for the home page and subpages. We are replacing the current website http://www.velmora-labs.com with a new website being built here: http://velmoraclean.com.stagehost.com/velmoraprime/. What we have now on the site is the basic wire frame. This is the desired layout and pictures we want to use. We would like you to add some design elements to make the website more professional looking and polished. Please refer to the attached style guide to help you in choosing the color. The client does like the green leaf, which is included in the last page of style guide and may be good for a background image. While the Velmora logo and leaf are green, we do not want to overuse the color green. The client does own other technologies that we will be promoting on the site and the logos for these technologies are attached below. These logos are Tusk, Velmora-Prime, and Wisp. We will be using this website to promote the technologies, the markets the technologies serve; drinking water, medical devices, apparel and textiles, and architectural surfaces, and to promote the customer using these devices. Please make the design "clean" and not cluttered, as these technologies are used to fight "dirty things".
Updates

Hello Designers! Thank you all very much for your design submissions. They were simply excellent. Due to the Holidays and New Years, many of the client's team members have been on vacation. We expect to have feedback shortly and pick the top design soon there after. Again, thank you all very much and hope the New Year brings you continued success. Best, Dorian

Industry/Entity Type

Biotechnology

Coding

Coded - Design and coding required

```html
<!DOCTYPE html>
<html lang="en">
<head>
<meta charset="utf-8">
<title>Velmora Antimicrobial</title>
<link href="https://fonts.googleapis.com/css2?family=Open+Sans:wght@400;600&family=Raleway:wght@400;500;600&family=Ubuntu:wght@300;400;500&display=swap" rel="stylesheet">
<style>
:root{
  --green:#63bb1a;
  --green-light:#8ccb58;
  --green-dark:#58a817;
  --green-title:#6cc127;
  --nav:#1f1f1f;
  --nav-line:#3a3a3a;
  --text:#666;
  --heading:#333;
  --orange:#e2731f;
  --muted:#999;
  --rule:#e3e3e3;
  --white:#fff;
}
*{margin:0;padding:0;box-sizing:border-box}
html,body{width:1031px;height:1200px;overflow:hidden;background:var(--white)}
body{position:relative;font-family:'Open Sans',sans-serif;color:var(--text)}
.abs{position:absolute}
.brand{left:110px;top:22px;font-family:'Raleway',sans-serif;font-weight:600;font-size:40px;color:var(--green);line-height:48px;letter-spacing:-0.5px}
.search{left:755px;top:53px;width:169px;height:23px;border:1px solid #ddd;font-family:'Ubuntu',sans-serif;font-style:italic;font-size:9px;color:#555;padding:6px 9px}
.search svg{position:absolute;right:6px;top:4px}
.nav{left:107px;top:87px;width:817px;height:37px;background:linear-gradient(#2c2c2c,#161616);display:flex;font-family:'Raleway',sans-serif;font-weight:500;font-size:13px;color:var(--white)}
.nav span{display:flex;align-items:center;justify-content:center;border-right:1px solid var(--nav-line);height:100%}
.nav span:last-child{border:none}
.hero{left:107px;top:124px;width:817px;height:363px;background:linear-gradient(100deg,#f1f1f1 0%,#e6e6e6 35%,#e87a2a 46%,#f0a066 52%,#dcdcdc 62%,#efefef 100%)}
.hero-box{left:141px;top:238px;width:319px;height:134px;background:var(--green-light);color:var(--white);font-family:'Ubuntu',sans-serif;padding:21px 22px}
.hero-box h1{font-weight:400;font-size:24px;line-height:28px}
.hero-box h2{font-weight:300;font-size:18px;line-height:22px}
.hero-box p{font-family:'Open Sans',sans-serif;font-size:9px;line-height:15px;margin-top:10px;padding-left:3px}
.dots{left:490px;top:468px;display:flex;gap:3px}
.dots i{width:10px;height:10px;border-radius:50%;background:var(--white)}
.market{top:505px;width:196px}
.market .photo{height:99px;border:1px solid #ddd}
.market h3{font-family:'Raleway',sans-serif;font-weight:500;font-size:15px;color:var(--green-title);margin-top:9px;line-height:18px}
.market p{font-size:9.5px;line-height:15.5px;margin-top:3px}
.market a{display:block;font-family:'Raleway',sans-serif;font-weight:600;font-size:10.5px;color:#444;margin-top:4px;text-decoration:none}
.rule{left:107px;top:713px;width:818px;height:1px;background:var(--rule)}
.welcome{left:110px;top:752px;width:520px}
.welcome h2{font-family:'Raleway',sans-serif;font-weight:400;font-size:21px;color:var(--heading)}
.welcome .lead{font-size:11px;color:#555;margin-top:6px}
.welcome p{font-size:9.5px;line-height:15.5px;margin-top:10px}
.partners{left:110px;top:940px;display:flex;gap:46px;font-family:'Raleway',sans-serif;font-weight:600;font-size:26px;letter-spacing:1px}
.partners .tusk{color:#d9393b}
.partners .prime{color:#222}
.partners .wisp{color:#1f6db3}
.news{left:672px;top:750px;width:240px}
.news h2{font-family:'Raleway',sans-serif;font-weight:400;font-size:18px;color:var(--heading);margin-bottom:10px}
.news .item{margin-bottom:10px;padding-left:2px}
.news h4{font-weight:400;font-size:9.5px;color:var(--orange)}
.news p{font-size:9.5px;line-height:15.5px;margin-top:2px}
.news time{display:block;font-size:9px;color:var(--muted);margin-top:3px}
.footer{left:0;top:1009px;width:1031px;height:152px;background:var(--green);color:var(--white);font-family:'Ubuntu',sans-serif;font-size:10px}
.fcol{top:26px;line-height:19px;border-right:1px solid rgba(255,255,255,.3);height:87px}
.fcol.last{border:none;line-height:17px}
.social{left:516px;top:101px;display:flex;gap:9px}
.social i{width:14px;height:14px;border-radius:50%;background:var(--white)}
.fbrand{left:776px;top:50px;font-family:'Raleway',sans-serif;font-weight:600;font-size:36px}
.bottom{left:0;top:1161px;width:1031px;height:39px;background:var(--green-dark);color:var(--white);font-family:'Ubuntu',sans-serif;font-size:8.5px;padding:15px 107px}
</style>
</head>
<body>
<div class="abs brand">Velmora</div>
<div class="abs search">Search here..
  <svg width="14" height="14" viewBox="0 0 14 14"><circle cx="6" cy="6" r="4.5" fill="none" stroke="#bbb" stroke-width="1.6"/><line x1="9.3" y1="9.3" x2="13" y2="13" stroke="#bbb" stroke-width="2"/></svg>
</div>
<nav class="abs nav">
  <span style="width:86px">Home</span><span style="width:91px">About Us</span><span style="width:84px">Markets</span><span style="width:106px">Technology</span><span style="width:154px">Customer Programs</span><span style="width:139px">News Highlights</span><span style="width:157px">Contact Us</span>
</nav>
<div class="abs hero" role="img" aria-label="Laboratory test tubes with orange liquid in a rack"></div>
<div class="abs hero-box">
  <h1>Antimicrobial Technology</h1>
  <h2>Class aptent taciti sociosqu</h2>
  <p>libero a tempus libero lectus feugiat felis Morbi diam<br>mauris viverra in gravida eu mattis in ante</p>
</div>
<div class="abs dots"><i></i><i></i><i></i><i></i></div>

<div class="abs market" style="left:108px">
  <div class="photo" role="img" aria-label="Water droplet splashing into blue water" style="background:linear-gradient(#dbeaf8,#7fb1e3)"></div>
  <h3>Drinking Water</h3><p>Morbi ornare gravida elit Integer congue augue et malesuada iaculis ipsum dui</p><a>Read More</a>
</div>
<div class="abs market" style="left:315px">
  <div class="photo" role="img" aria-label="Nurse caring for a young patient in a hospital bed" style="background:linear-gradient(#e4e6dc,#b9c9c2)"></div>
  <h3>Medical Services</h3><p>Morbi ornare gravida elit Integer congue augue et malesuada iaculis ipsum dui</p><a>Read More</a>
</div>
<div class="abs market" style="left:522px">
  <div class="photo" role="img" aria-label="Textile factory floor with weaving machines and pink fabric" style="background:linear-gradient(#8a7a66,#c97a86)"></div>
  <h3>Apparel &amp; Textiles</h3><p>Morbi ornare gravida elit Integer congue augue et malesuada iaculis ipsum dui</p><a>Read More</a>
</div>
<div class="abs market" style="left:729px">
  <div class="photo" role="img" aria-label="Worker in white protective clothing at a packaging line" style="background:linear-gradient(#f2f2f2,#c9b28c)"></div>
  <h3>Architectural Surfaces</h3><p>Morbi ornare gravida elit Integer congue augue et malesuada iaculis ipsum dui</p><a>Read More</a>
</div>

<div class="abs rule"></div>

<section class="abs welcome">
  <h2>Welcome to Velmora Antimicrobial</h2>
  <div class="lead">Morbi ornare gravida elit Integer congue augue et malesuada iaculis ipsum dui aliquet</div>
  <p>Morbi diam mauris viverra in gravida eu mattis in ante Morbi eget arcu Morbi porta libero id ullamcorper nonummy nibh ligula pulvinar metus eget consectetuer augue nisi quis lacus Ut ac mi quis lacus mollis aliquam Curabitur iaculis tempus eros Curabitur vel mi sit amet magna malesuada ultrices Ut nisi erat fermentum vel</p>
  <p>Congue id euismod in elit Fusce ultricies orci ac feugiat suscipit leo massa sodales velit et scelerisque mi tortor at ipsum Morbi diam mauris viverra in gravida eu mattis in ante Morbi eget arcu Morbi porta libero id ullamcorper nonummy nibh ligula pulvinar metus eget consectetuer augue nisi quis lacus Ut ac mi Class aptent taciti sociosqu ad conubia nostra per inceptos hymenaeos Proin nulla arcu nonummy luctus dictum eget fermentum</p>
</section>
<div class="abs partners"><span class="tusk">TUSK</span><span class="prime">PRIME</span><span class="wisp">WISP</span></div>

<aside class="abs news">
  <h2>NEWS &amp; EVENTS</h2>
  <div class="item"><h4>Morbi porta libero ullamcorper</h4><p>Integer congue augue et malesuada iaculis ipsum dui aliquet felis at cursus magna nisl nec elit Praesent</p><time>Posted on 12 Nov 2014</time></div>
  <div class="item"><h4>Class aptent taciti sociosqu</h4><p>Integer congue augue et malesuada iaculis ipsum dui aliquet felis at cursus magna nisl nec elit</p><time>Posted on 12 Nov 2014</time></div>
  <div class="item"><h4>Morbi ornare gravida</h4><p>Integer congue augue et malesuada iaculis ipsum</p><time>Posted on 12 Nov 2014</time></div>
</aside>

<footer class="abs footer">
  <div class="abs fcol" style="left:109px;width:109px">About Company<br>What We Do<br>How We Work<br>Our Projects</div>
  <div class="abs fcol" style="left:251px;width:106px">Testimonials<br>News &amp; Blog Post<br>Support<br>Video</div>
  <div class="abs fcol" style="left:389px;width:91px">Term of Use<br>Contact Us<br>Sitemap</div>
  <div class="abs fcol last" style="left:516px;width:200px">48 Larkfield Road #3B<br>Ohio 40127 OH<br>555.014.2290<br>info@brightquill.com</div>
  <div class="abs social"><i></i><i></i><i></i><i></i></div>
  <div class="abs fbrand">Velmora</div>
</footer>
<div class="abs bottom">© 2014 Company Name &nbsp;All right reserved &nbsp;Term of Use</div>
</body>
</html>
```